ALL I NEED IS A BUSINESS CARD AND LETTER HEAD OFFICIAL PAPER

i only need a letter head ( sample attached)
along with business cards.
i will upload a sample ,along with the logo of both companies that should be on the letter head and business cards.

Note:its a high end maritime solution company

Company name is Tormund Halvex Africa

slogan : For maritime solution ( it could be on the back side of the business card)

Project Deadline Extended Reason: Hi Guys, thanks for your designs , i am sorry but now we just changed the company name toLuerssen halvex Africa slogan For Maritime solutions. i hope you can help me with that! slogan could be in the back side or any place, but not next to the title . and both logos of halvex and tormund should be there. thank you Added Sunday, March 1, 2015

Industry/Entity Type

Business

Contact Information for Business Card

as attached, please provide more designs

Font styles to use
Serif

Requirements
Must have
• SAME AS THE BUSINESS LETTER,
• Tormund Halvex Africa
• slogan for Maritime Solutions

```html
<!DOCTYPE html>
<html lang="en">
<head>
<meta charset="utf-8">
<title>Tormund Halvex Africa – Letterhead</title>
<link rel="stylesheet" href="https://fonts.googleapis.com/css2?family=EB+Garamond:wght@400;500&display=swap">
<style>
  :root {
    --brand-blue: #0a72d1;
    --brand-navy: #1a4a72;
    --ink-navy: #1c3566;
    --paper: #ffffff;
    --on-blue: #ffffff;
  }
  * { margin: 0; padding: 0; box-sizing: border-box; }
  html, body {
    width: 849px;
    height: 1200px;
    overflow: hidden;
    background: var(--paper);
  }
  .letterhead {
    position: relative;
    width: 849px;
    height: 1200px;
    background: var(--paper);
    font-family: "EB Garamond", Georgia, serif;
    overflow: hidden;
  }
  .decor {
    position: absolute;
    inset: 0;
    width: 849px;
    height: 1200px;
  }
  .brand {
    position: absolute;
    left: 27px;
    top: 66px;
    display: flex;
    align-items: center;
    gap: 12px;
  }
  .brand-name {
    font-size: 27px;
    font-weight: 500;
    letter-spacing: 1.5px;
    color: var(--ink-navy);
    line-height: 1;
  }
  .brand-mark {
    width: 22px;
    height: 22px;
    background: var(--brand-blue);
  }
  .company-title {
    position: absolute;
    left: 28px;
    top: 113px;
    font-size: 20px;
    font-weight: 400;
    line-height: 22px;
    color: var(--ink-navy);
    letter-spacing: 0.2px;
  }
  .contact {
    position: absolute;
    color: var(--on-blue);
    font-size: 18px;
    line-height: 1;
    white-space: nowrap;
  }
  .contact-web { left: 587px; top: 1118px; }
  .contact-email { left: 395px; top: 1161px; }
  .contact-phone { left: 684px; top: 1161px; }
</style>
</head>
<body>
<div class="letterhead">
  <svg class="decor" viewBox="0 0 849 1200" aria-hidden="true">
    <path class="top-band" fill="var(--brand-blue)"
      d="M0 0 H849 V84 C640 40 320 20 0 28 Z"/>
    <path class="bottom-band" fill="var(--brand-blue)"
      d="M0 1160 C260 1168 560 1110 849 1104 V1200 H0 Z"/>
    <path class="bottom-stripe" fill="var(--brand-navy)"
      d="M98 1152 C340 1146 600 1070 849 1066 V1097 C600 1094 360 1150 98 1152 Z"/>
  </svg>

  <header class="brand">
    <span class="brand-name">TORMUND HALVEX</span>
    <span class="brand-mark"></span>
  </header>

  <h1 class="company-title">TORMUND HALVEX AFRICAN<br>MARITIME SOLUTIONS</h1>

  <footer>
    <p class="contact contact-web">www.tormundhalvex.com</p>
    <p class="contact contact-email">Email: info@tormundhalvex.com</p>
    <p class="contact contact-phone">Tel: (021) 555-0142</p>
  </footer>
</div>
</body>
</html>
```